Commercial Rooftop Solar business needs a website

We need a website with fantastic appeal for a new company based in Melbourne called Brightvale Energy. We design and install solar energy systems for commercial applications across Australia. Our market is to focus on small to medium businesses looking for solar solutions, but we will also provide our service for residential customers. We would like a beautiful 'front page' feel to our home page, using photographs of solar PV systems and/or natural imagery. Our logo uses the colours orange and black, which could easily be echoed in photographic imagery of sunset and sunrise, for example. The design should communicate quiet confidence and professionalism to a corporate marketplace.

NEW POINTS FOR BRIEF: This design also needs to be flexible to allow for additional future content, including a Support page with sub pages, FAQ's, and a Blog.

As part of this design project, we will require the coding for the website to be completed by the designer.

We have seen some websites, which we like the look and feel of: these are listed below.

keenroofpower.com.au:

• Beautiful images underlaying brief text selling points.
• Simple ‘front cover’ style home page with elegant drop-down menu, stylish simple font style.
• Home page invites exploration through the menu links, rather than trying to provide all the information up front.
• Company logo and name in the top left hand corner, contact details accessible at top right hand, seems consistent in most sites.

tolvaenergy.com.au

brinkeltpower.com:
• Same element as the others is the front-page style home page with beautiful images underlying text.

We have a webpage that we started uploading content to. You can use some of the content there in your designs: www.brightvaleenergy.com.au

Technical Specifications:
PAGES:

Home

About Us

Solutions - Commercial
- Residential

Products - Solar Panels - Morvo Falcon, Morvo CELT, Morvo KT
- Solar Inverters - Valtrex, SunPivot
- Monitoring systems - Lumen Metrics
- Batteries - QD

- Datasheets have been provided for reference but if it's too much work, you can use generic text and we will provide content later.

Contact Us

FUTURE PAGES (Please consider in structure, where links could be placed):

Support

FAQ's

Blog.

We could provide some content for the Support page soon, but the Blog and FAQ's are future pages which we don't want highlighted in the design as we don't yet have content.

Phone: 1800 7 VOLTA
Email: sales@brightvaleenergy.com.au

Currently, I do not have images and text available. Please
use placeholders in the meantime. The final text and images will be uploaded for the winner once a winning design has been selected.

Target Market(s)

Primary focus is on small to medium sized business owners. Those owners will have a house which may be suitable for solar so we want to cater to residential deeper in the website.

Industry/Entity Type

Solar Energy

Coding

Coded - Design and coding required

Number of Pages Required

5+ page

Colors
f78f20
0255a3

Requirements
Must have
• Logo as per attachments.
Nice to have
• Logo can have alternate colours Eg. White on Orange or Black etc. provided colour correct logo is shown somewhere eg. footer or contact page.
• In the active site, I'd like to have:
• Very slowly zooming images - barely perceptible.
• Title text that rolls into place
• Subtle movements
• See https://paylarkfinance.com.au/ for example

```html
<!DOCTYPE html>
<html lang="en">
<head>
<meta charset="utf-8">
<title>Brightvale Energy</title>
<link rel="stylesheet" href="https://fonts.googleapis.com/css2?family=Ubuntu:wght@400;500&family=Open+Sans:ital,wght@0,400;0,600;1,400&family=Roboto:wght@400;500&display=swap">
<style>
:root{
  --orange:#f05a28;
  --orange-soft:#f47a4d;
  --charcoal:#333333;
  --charcoal-deep:#2b2b2b;
  --footer:#6c6c6c;
  --mist:#eef2f8;
  --ink:#222222;
  --text-grey:#555555;
  --ghost:rgba(0,0,0,.05);
  --ghost-light:rgba(255,255,255,.07);
  --white:#ffffff;
  --line:#c9ced6;
}
*{box-sizing:border-box;margin:0;padding:0}
html,body{width:1200px;height:2975px;overflow:hidden;background:var(--white)}
body{position:relative;font-family:"Open Sans",sans-serif;color:var(--ink)}
.abs{position:absolute}
svg.band{position:absolute;left:0;top:0;width:1200px;height:2975px}

/* header */
.hero-photo{left:0;top:0;width:1200px;height:600px;
  background:linear-gradient(180deg,#c9d3dc 0%,#9fb0a8 28%,#7d8a8f 45%,#5b6672 70%,#8c96a2 100%)}
.brand{left:80px;top:44px;display:flex;align-items:center;gap:10px;
  font-family:"Ubuntu",sans-serif;font-weight:500;font-size:22px;color:var(--orange)}
.brand-dot{width:28px;height:28px;border-radius:50%;background:var(--charcoal)}
.main-nav{left:540px;top:36px;width:640px;display:flex;justify-content:space-around;
  font-family:"Ubuntu",sans-serif;font-size:17px;color:var(--white)}

/* section headings */
.ghost-title{left:0;width:1200px;text-align:center;font-family:"Ubuntu",sans-serif;
  font-size:104px;line-height:1;color:var(--ghost)}
.ghost-title.on-dark{color:var(--ghost-light)}
.section-title{left:0;width:1200px;text-align:center;font-family:"Ubuntu",sans-serif;
  font-weight:500;font-size:38px;line-height:1;color:var(--ink)}
.section-title.on-dark{color:var(--white)}
.title-rule{left:330px;width:540px;height:2px;
  background:linear-gradient(90deg,transparent,var(--line) 30%,var(--orange) 50%,var(--line) 70%,transparent)}
.emblem{width:62px;height:62px;border-radius:50%;background:var(--orange);left:569px;border:6px solid var(--white)}

/* about */
.about-copy{left:150px;width:900px;text-align:center;font-style:italic;font-size:13.5px;
  line-height:1.5;color:var(--text-grey)}
.about-copy p{margin-bottom:16px}
.about-copy a{color:var(--ink);font-weight:600;text-decoration:underline}
.btn-outline{display:block;text-align:center;font-family:"Ubuntu",sans-serif;font-size:15px;
  border:1.5px solid var(--orange);color:var(--orange);border-radius:3px;line-height:32px}

/* solutions */
.solution{width:310px;color:var(--white)}
.solution h3{font-family:"Ubuntu",sans-serif;font-weight:500;font-size:19px;color:var(--orange);margin-bottom:14px}
.solution p{font-style:italic;font-size:13.5px;line-height:1.55;height:84px;overflow:hidden}
.btn-light{margin-top:28px;width:132px;text-align:center;border:1.5px solid #ddd;color:var(--white);
  font-family:"Ubuntu",sans-serif;font-size:15px;line-height:30px}
.divider{width:1px;background:var(--orange);opacity:.7}

/* products */
.product{width:308px;height:477px;background:var(--white);box-shadow:0 0 0 1px #e3e3e3,0 4px 10px rgba(0,0,0,.08)}
.product-photo{position:absolute;left:60px;top:22px;width:190px;height:300px;
  background:linear-gradient(180deg,#2d3a63,#1f2a4a)}
.product-photo.dark{background:linear-gradient(180deg,#1d1d22,#0d0d10)}
.product-label{position:absolute;left:10px;top:338px;width:298px;height:139px;padding-top:24px;
  text-align:center;color:var(--white);font-family:"Ubuntu",sans-serif;font-size:19px;line-height:1.45;
  clip-path:polygon(0 14px,92% 0,92% 0,100% 10%,100% 78%,84% 100%,0 100%)}
.product-label.orange{background:var(--orange)}
.product-label.dark{background:var(--charcoal)}
.buy{display:inline-block;margin-top:10px;width:110px;line-height:26px;border-radius:3px;
  font-family:"Open Sans",sans-serif;font-style:italic;font-size:13px}
.orange .buy{background:var(--charcoal-deep);font-style:normal;font-family:"Ubuntu",sans-serif}
.dark .buy{background:var(--orange)}

/* contact */
.contact-title{left:0;width:1200px;text-align:center;font-family:"Roboto",sans-serif;font-size:44px;line-height:1;color:var(--ink)}
.field{height:44px;background:var(--white);border:1px solid #cfd5de;border-radius:3px;
  font-family:"Roboto",sans-serif;font-size:14px;color:#8a8f96;padding:13px 12px}
.comment{height:96px}
.send{position:absolute;right:18px;bottom:26px}
.submit{left:532px;top:2588px;width:136px;line-height:34px;text-align:center;background:var(--orange);
  color:var(--white);border-radius:3px;font-family:"Roboto",sans-serif;font-weight:500;font-size:17px}

/* footer */
.footer{left:0;top:2757px;width:1200px;height:218px;background:var(--footer)}
.footer-brand{left:120px;top:2880px;display:flex;align-items:center;gap:10px;
  font-family:"Ubuntu",sans-serif;font-weight:500;font-size:30px;color:var(--orange)}
.footer-brand .brand-dot{width:34px;height:34px;background:var(--charcoal)}
.footer-col{top:2815px;font-family:"Roboto",sans-serif;font-size:16px;line-height:21px;color:var(--white)}
.footer-col h4{font-weight:500;font-size:16px;color:var(--white)}
.footer-col.links{font-size:15px;line-height:21px}
.footer-col.links h4{font-size:15px}
.social li{list-style:none;display:flex;align-items:center;gap:8px}
.social .icon{width:13px;height:13px;border-radius:50%;background:var(--white)}
.copyright{left:0;top:2952px;width:1200px;text-align:center;font-size:11px;color:#eee}
</style>
</head>
<body>

<div class="abs hero-photo" role="img" aria-label="Two engineers in hard hats reviewing a rooftop of solar panels with hills behind"></div>

<svg class="band" viewBox="0 0 1200 2975" aria-hidden="true">
  <!-- nav band -->
  <polygon points="330,60 560,30 1200,30 1200,92 1150,90 1120,82 500,84 360,80" fill="var(--orange)"/>
  <!-- about white sheet -->
  <polygon points="0,596 310,500 560,505 1200,492 1200,870 880,866 860,880 0,880" fill="var(--white)"/>
  <!-- solutions dark -->
  <polygon points="0,915 380,905 400,898 880,890 1200,855 1200,1300 900,1318 620,1335 300,1370 0,1400" fill="var(--charcoal)"/>
  <!-- contact mist -->
  <polygon points="0,2125 300,2122 320,2130 1200,2120 1200,2715 900,2718 880,2730 0,2740" fill="var(--mist)"/>
</svg>

<header>
  <div class="abs brand"><span class="brand-dot"></span>Brightvale Energy</div>
  <nav class="abs main-nav"><span>Home</span><span>About Us</span><span>Solutions</span><span>Products</span><span>Contact Us</span></nav>
</header>

<section class="about">
  <div class="abs emblem" style="top:482px"></div>
  <div class="abs ghost-title" style="top:525px">About Us</div>
  <h2 class="abs section-title" style="top:603px">About Us</h2>
  <div class="abs title-rule" style="top:648px"></div>
  <div class="abs about-copy" style="top:668px">
    <p>Brightvale Energy is a national company that specialises in solar solutions for the commercial market. We also provide solutions for the residential market, bringing our uncompromising quality and service to the home.</p>
    <p>The founder of the company has over 10 years experience delivering projects on both a residential and commercial scale, having overseen the installation of more than 3 megawatts of solar projects. They were a pioneer on the <a>first megawatt scale project</a> in Australia.</p>
    <p>As a leader in the field, we offer cutting edge solar technology backed by industry leading warranties. All our systems are designed and installed by <a>Green Power Guild</a> accredited persons. Our award winning designer will ensure your system will give the best long term performance and return on investment.</p>
  </div>
  <a class="abs btn-outline" style="left:532px;top:840px;width:136px">Learn More</a>
</section>

<section class="solutions">
  <div class="abs ghost-title on-dark" style="top:940px">Solutions</div>
  <h2 class="abs section-title on-dark" style="top:1006px">Solutions</h2>
  <div class="abs title-rule" style="top:1050px"></div>
  <div class="abs solution" style="left:98px;top:1092px">
    <h3>Brightvale specialises</h3>
    <p>In a sunburnt country, harnessing the immense power of the sun for the energy requirements of your business is the most practical solution to sustain your business for the long term.</p>
    <div class="btn-light">Learn More</div>
  </div>
  <div class="abs divider" style="left:418px;top:1090px;height:180px"></div>
  <div class="abs solution" style="left:452px;top:1092px">
    <h3>Business Case: No-Cost Solar</h3>
    <p>There's an incredibly sound business case to install solar for your business. With the current Government incentives, provided as up-front rebates based on Small-scale Technology.</p>
    <div class="btn-light">Learn More</div>
  </div>
  <div class="abs divider" style="left:765px;top:1090px;height:180px"></div>
  <div class="abs solution" style="left:795px;top:1092px">
    <h3>Sustainability: Our Environment</h3>
    <p>Protecting our planet protects all of us: our communities, our health and our future. Using sustainable energy ensures the longevity of our businesses too. Switching to solar power is.</p>
    <div class="btn-light">Learn More</div>
  </div>
</section>

<section class="products">
  <div class="abs emblem" style="top:1294px"></div>
  <div class="abs ghost-title" style="top:1378px">Products</div>
  <h2 class="abs section-title" style="top:1462px">Products</h2>
  <div class="abs title-rule" style="top:1505px"></div>

  <article class="abs product" style="left:85px;top:1563px">
    <div class="product-photo" role="img" aria-label="Blue polycrystalline solar panel"></div>
    <div class="product-label orange">Morvo Falcon -<br>The budgetwortkhorse<br><span class="buy">Buy Now</span></div>
  </article>
  <article class="abs product" style="left:440px;top:1563px">
    <div class="product-photo" role="img" aria-label="Blue solar panel with optimiser badge"></div>
    <div class="product-label dark">Morvo Falcon MX -<br>Optimised and Flexible<br><span class="buy">Buy Now</span></div>
  </article>
  <article class="abs product" style="left:795px;top:1563px">
    <div class="product-photo dark" role="img" aria-label="Two black monocrystalline solar panels"></div>
    <div class="product-label dark">Morvo Falcon<br>PERC - Beautiful Power<br><span class="buy">Buy Now</span></div>
  </article>
</section>

<section class="contact">
  <div class="abs emblem" style="top:2135px"></div>
  <div class="abs ghost-title" style="top:2200px">Contact Us</div>
  <h2 class="abs contact-title" style="top:2293px">Contact Us</h2>
  <div class="abs title-rule" style="top:2342px"></div>
  <div class="abs field" style="left:147px;top:2385px;width:280px">First</div>
  <div class="abs field" style="left:452px;top:2385px;width:280px">Last...</div>
  <div class="abs field" style="left:756px;top:2385px;width:280px">Email</div>
  <div class="abs field comment" style="left:147px;top:2455px;width:889px">Comment...
    <svg class="send" width="18" height="18" viewBox="0 0 24 24" aria-hidden="true"><path d="M2 11 22 3 15 22 12 13Z M12 13 22 3" fill="none" stroke="#3b8fd6" stroke-width="2" stroke-linejoin="round"/></svg>
  </div>
  <div class="abs submit">Submit</div>
</section>

<footer>
  <div class="abs footer"></div>
  <div class="abs emblem" style="top:2675px"></div>
  <div class="abs footer-brand"><span class="brand-dot"></span>Brightvale Energy</div>
  <div class="abs footer-col" style="left:412px">
    <h4>Brightvale Energy</h4>
    <div>Terms of use</div><div>Buyer protection</div><div>Privacy</div><div>Security</div>
  </div>
  <div class="abs footer-col links" style="left:690px">
    <h4>Learn more</h4>
    <div>Home</div><div>About Us</div><div>Solution</div><div>Products</div><div>Contact Us</div>
  </div>
  <div class="abs footer-col" style="left:925px;top:2820px">
    <h4 style="margin-bottom:2px">Follow us</h4>
    <ul class="social">
      <li><span class="icon"></span>Snapfeed</li>
      <li><span class="icon"></span>Friendbook</li>
      <li><span class="icon"></span>Chirper</li>
    </ul>
  </div>
  <div class="abs copyright">© 2017 All Rights Reserved</div>
</footer>

</body>
</html>
```